Flyer-Design für Hundephysiopraxis
Zielgruppe
Ich bin selbstständige Hundephysiotherapeutin / Hundeosteopathin /Hundefitnesstrainerin. Meine Zielgruppe sind Hundehalter bzw. allgemein Tierhalter (biete noch weitere Dinge für Hunde/Tiere an) aber auch Tierärzte.
Aufgabenstellung
Es wäre schön, wenn Sie die Texte ähnlich wie auf meiner Homepage gestalten (z.B. Infos aus der Startseite oder Therapieformen).
Prinzipiell sollte es eher natürlich, freundlich und nett gestaltet sein. Schlichtere Farben passend zum Logo.
Homepage: www.pfotenruhe-mitte.de
Bei den Maßen bin ich offen, hatte aber eher an diesen 'typischen Flyer' gedacht (3 seitiger Flyer mit Vorder und Rückseite) bin aber prinzipiell offen :)
Einen Beispiel Flyer habe ich drangehängt sowie z.B. schon ein paar Fotos die man ggf nutzen kann. Weitere Behandlunsfotos kann ich gerne nachreichen.
Die Flyer sollen hauptsächlich bei z.B. Tierärzten / Tierklinik / Tiernahrungsmärkte wie Napfkorb ausgelegt werden damit Menschen die mich noch nicht kennen auf meine Arbeit aufmerksam werden.

```html
<!DOCTYPE html>
<html lang="de">
<head>
<meta charset="utf-8">
<title>Pfotenruhe Mitte – Faltflyer</title>
<link href="https://fonts.googleapis.com/css2?family=Bitter:wght@500;700&family=Source+Serif+4:ital,wght@0,400;0,600;0,700;1,400&display=swap" rel="stylesheet">
<style>
:root{
  --stage:#d9d9d9;
  --blue:#9dc3d6;
  --mauve:#9a757b;
  --mauve-text:#946b74;
  --beige:#e6e0dc;
  --beige-dark:#d8d1cc;
  --white:#fbfaf9;
  --orange:#cf7a3e;
  --teal:#3b93a8;
  --body:#5c4a4e;
}
*{margin:0;padding:0;box-sizing:border-box}
html,body{width:1200px;height:900px;overflow:hidden;background:var(--stage)}
body{position:relative;font-family:"Source Serif 4",Georgia,serif;color:var(--body)}
.sheet{position:absolute;left:130px;width:940px;height:316px;overflow:hidden;box-shadow:0 10px 18px rgba(0,0,0,.18)}
.sheet--outside{top:70px}
.sheet--inside{top:500px}
.sheet svg.backdrop{position:absolute;inset:0;width:940px;height:316px}
.txt{position:absolute;font-size:7px;line-height:1.4}
.txt p+p{margin-top:7px}
h2{font-family:"Bitter",Georgia,serif;font-weight:700;line-height:1.12}

/* outside */
.about-title{left:25px;top:20px;color:var(--mauve-text)}
.about-title h2{font-size:20px}
.about-title .name{font-family:"Bitter",serif;font-weight:500;font-size:15px;margin-top:2px}
.about-text{left:25px;top:178px;width:178px;color:var(--mauve-text)}
.brand{position:absolute;text-align:center;color:var(--orange);font-weight:700}
.brand .mark{display:block;margin:0 auto;border:2px solid var(--orange);border-radius:50%}
.brand--small{left:313px;width:314px;top:45px;font-size:11px}
.brand--small .mark{width:46px;height:46px;margin-bottom:5px}
.brand--large{left:627px;width:313px;top:28px;font-size:16px}
.brand--large .mark{width:72px;height:72px;margin-bottom:6px}
.contact{left:313px;width:314px;top:187px;text-align:center;color:#fff;font-size:7.2px}
.contact .firm{font-weight:700;font-size:8px}
.contact .sub{font-size:8.5px}
.contact p+p{margin-top:8px}

/* inside */
.move-head{left:113px;top:32px;color:var(--teal);font-size:12.5px}
.move-text{left:128px;top:90px;width:168px;text-align:center}
.move-text .p2{padding-left:18px}
.move-text .p3{padding-left:44px;text-align:left}
.physio-head{left:348px;top:31px;color:var(--mauve-text);font-size:12.5px}
.physio-text{left:348px;top:73px;width:200px}
.physio-text .intro{width:168px}
.physio-text .goal{font-weight:600}
.quote{position:absolute;left:348px;top:253px;color:var(--mauve-text);font-style:italic;font-size:9.5px;line-height:1.3}
.quote .line2{padding-left:14px}
.quote cite{display:block;font-style:normal;font-size:5.5px;letter-spacing:.06em;color:var(--teal);margin-top:2px}
.vital-head{left:690px;width:130px;top:36px;text-align:center;color:var(--mauve-text);font-size:12px}
.vital-text{left:652px;width:160px;top:110px;text-align:right}
.services{left:652px;width:160px;top:198px;text-align:center;color:var(--teal);font-weight:700;font-size:6.6px}
</style>
</head>
<body>

<section class="sheet sheet--outside">
  <svg class="backdrop" viewBox="0 0 940 316" aria-hidden="true">
    <rect x="0" y="0" width="314" height="316" fill="var(--blue)"/>
    <rect x="314" y="0" width="313" height="316" fill="var(--white)"/>
    <path d="M314 100 C420 150 520 50 627 60 L627 316 L314 316 Z" fill="var(--beige)"/>
    <path d="M314 196 C400 160 520 160 627 185 L627 316 L314 316 Z" fill="var(--mauve)"/>
    <rect x="627" y="0" width="313" height="316" fill="var(--white)"/>
    <path d="M627 60 C720 120 840 40 940 70 L940 316 L627 316 Z" fill="var(--beige)"/>
  </svg>
  <svg class="backdrop" viewBox="0 0 940 316" role="img" aria-label="Porträtfoto der Therapeutin im Kreis">
    <circle cx="206" cy="82" r="89" fill="#cfcac6"/>
  </svg>
  <svg class="backdrop" viewBox="0 0 940 316" role="img" aria-label="Foto eines Hundes in einer blühenden Wiese">
    <defs><linearGradient id="meadow" x1="0" y1="0" x2="0" y2="1"><stop offset="0" stop-color="#8a8a78"/><stop offset="1" stop-color="#6f7a52"/></linearGradient></defs>
    <path d="M627 200 C720 170 820 140 940 150 L940 316 L627 316 Z" fill="url(#meadow)"/>
  </svg>

  <div class="txt about-title"><h2>Über mich</h2><div class="name">Marlene Voss</div></div>
  <div class="txt about-text">
    <p>Für mich steht Dein Hund an erster Stelle! Als gelernte Hundephysiotherapeutin und Hundemasseurin helfe ich Deinem Hund dabei, die Gesundheit und damit die Lebensqualität und Lebensfreude zurück zu erhalten.</p>
    <p>Ich habe selbst Erfahrungen mit Tierschutzhunden, sowie Hunden aus deutscher Zucht und weiß, dass manche Hunde „ihr Päckchen“ zu tragen haben. Umso mehr möchte ich, dass sich Dein Vierbeiner bei mir wohlfühlt, er mir Vertrauen schenkt und gerne zur Physiotherapie geht.</p>
  </div>

  <div class="brand brand--small"><span class="mark"></span>Pfotenruhe Mitte</div>
  <div class="txt contact">
    <p><span class="firm">Pfotenruhe Mitte</span><br><span class="sub">Hundephysiotherapie</span></p>
    <p>Marlene Voss<br>Lindenweg 7<br>35390 Talheim</p>
    <p>info@pfotenruhe-mitte.de<br>Mobil: 0171 5550142</p>
    <p>www.pfotenruhe-mitte.de</p>
  </div>
  <div class="brand brand--large"><span class="mark"></span>Pfotenruhe Mitte</div>
</section>

<section class="sheet sheet--inside">
  <svg class="backdrop" viewBox="0 0 940 316" aria-hidden="true">
    <rect x="0" y="0" width="940" height="316" fill="var(--beige)"/>
    <line x1="313" y1="0" x2="313" y2="316" stroke="var(--beige-dark)" stroke-width="1"/>
    <path d="M690 0 L940 0 L940 316 L548 316 C548 250 590 215 620 175 C650 135 700 80 690 0 Z" fill="var(--blue)"/>
  </svg>
  <svg class="backdrop" viewBox="0 0 940 316" role="img" aria-label="Foto eines rennenden Schäferhundes auf einem Feldweg">
    <defs><linearGradient id="runner" x1="0" y1="0" x2="0" y2="1"><stop offset="0" stop-color="#5f6a3e"/><stop offset="1" stop-color="#8a7a55"/></linearGradient></defs>
    <path d="M0 0 L97 0 C90 90 150 170 155 316 L0 316 Z" fill="url(#runner)"/>
  </svg>
  <svg class="backdrop" viewBox="0 0 940 316" role="img" aria-label="Foto einer Hand, die eine Hundepfote hält">
    <circle cx="608" cy="65" r="88" fill="#c7b8a8"/>
  </svg>
  <svg class="backdrop" viewBox="0 0 940 316" role="img" aria-label="Foto einer Frau, die einen hellen Labrador umarmt">
    <defs><linearGradient id="hug" x1="0" y1="0" x2="0" y2="1"><stop offset="0" stop-color="#6f7356"/><stop offset="1" stop-color="#b7a98f"/></linearGradient></defs>
    <path d="M838 0 L940 0 L940 316 L808 316 C822 230 818 120 838 0 Z" fill="url(#hug)"/>
  </svg>

  <h2 class="txt move-head">Leben ist Bewegung<br>&nbsp;und Bewegung ist<br>&nbsp;&nbsp;Lebensqualität!</h2>
  <div class="txt move-text">
    <p>Rennen, laufen, springen, toben und spielen. Wer keine Schmerzen hat, kann sich frei bewegen und hat Spaß dabei. Wenn unsere Hunde jedoch erkranken oder alt werden, dann benötigen sie unsere Unterstützung.</p>
    <p class="p2">Nach einem Unfall, bei Schmerzen im Rücken oder Beschwerden in den Gelenken, nach Operationen oder bei Lahmheiten können Physiotherapie sowie Osteopathie helfen.</p>
    <p class="p3">Schmerzen werden gelindert, verspannte Muskulatur gelockert, die Beweglichkeit verbessert und wieder hergestellt. Physiotherapie baut Muskulatur auf, fördert die Genesung und hilft im Alter fit zu bleiben.</p>
  </div>

  <h2 class="txt physio-head">Hundephysiotherapie &amp;<br>Hundeosteopathie (i.A.)</h2>
  <div class="txt physio-text">
    <p class="intro">Jeder Körper ist ein individuelles und komplexes System mit eigenen Anforderungen an Beanspruchungen, Intensitäten und Erholungsphasen. Entsprechend umfangreich aufgestellt ist das Therapiespektrum meiner Arbeit.</p>
    <p>Dabei immer im Fokus: Die stets vollkommen individuellen Therapieprogramme, in enger Zusammenarbeit mit dem Tierarzt. Sensibel abgestimmt auf die spezifischen Anforderungen der einzelnen Krankheitsbilder. Jeder Hund hat eine andere Hintergrundgeschichte und auch dies berücksichtige ich bei meinen Therapien.</p>
    <p class="goal">Mein Ziel ist es, die Lebensfreude und Lebensqualität unserer Vierbeiner zu erhalten oder gar zu verbessern.</p>
  </div>
  <blockquote class="quote">„Lebensfreude lässt sich am<br><span class="line2">besten von Hunden lernen.“</span><cite>JONAS FELDMANN</cite></blockquote>

  <h2 class="txt vital-head">Doch nicht nur<br>die Hundephysio-<br>therapie verhilft<br>zu mehr Vitalität</h2>
  <div class="txt vital-text">
    <p>Ist Dein Hund ängstlich, ihm geht es nicht gut oder Du wirst aus verschiedenen Verhaltensweisen nicht schlau? Du möchtest die Fitness Deines Hundes verbessern oder ein paar Kilos sollen schwinden?</p>
    <p>Gemeinsam finden wir die passende Behandlungsmethode!</p>
  </div>
  <div class="txt services">Hundephysiotherapie · Hundeosteopathie ·<br>Hundefitness · Bachblütenberatung ·<br>Blutegeltherapie · Tierkommunikation ·<br>Mykotherapie · Edelsteintherapie</div>
</section>

</body>
</html>
```